Ferncastle Holdings - stationery for luxury, exclusive property investment company

We need stationery (letterhead, folder, compliments slip and envelope) and business cards which will reflect our luxury brand.

I have attached some design examples that we like.

We are an investment company which buys property to provide accommodation for corporate customers.

The design of the stationery needs to be be simple, refined, understated, luxury and very tasteful.

The design should communicate luxury and exclusivity, without being ostentatious.

Logo files are attached

Please can designers re-read the brief, and make sure the logo is in gold on either on a navy or white background.

Target Market(s)

Wealthy customers

Contact Information for Business Card

Helen Travers-Booth
Director
Ferncastle Holdings Limited
email: helen@ferncastleholdings.co.uk
mob: 07712645930

Font styles to use
Serif

Colors

Designer to choose colors to be used in the design.

Requirements
Must have
• The logo must be gold on either a white or navy background as per the attached logos.
• The stationery MUST have the following information:
• Ferncastle Holdings Limited
• The Willows
• Ashby Rise
• Ashby
• GL52 7TN
• Company Number: 20418736 (Registered in England and Wales)
• The letterhead must also have the two attached logos for the PLG and the PLG accreditation scheme. They do not need to be large.
Nice to have
• A watermark, navy banding either top or bottom.
Should not have
• Anything that looks budget.

```html
<!DOCTYPE html>
<html lang="en">
<head>
<meta charset="utf-8">
<title>Ferncastle Holdings – Business Card</title>
<link rel="stylesheet" href="https://fonts.googleapis.com/css2?family=Roboto:wght@400;700&display=swap">
<style>
  :root {
    --backdrop: #b9bdbe;
    --card: #f6f5f1;
    --gold: #b38a2a;
    --gold-edge: #a7892f;
    --ink: #1d1d1d;
    --muted: #6d6d6d;
    --badge-red: #c4141c;
  }
  * { box-sizing: border-box; margin: 0; padding: 0; }
  html, body { width: 1200px; height: 824px; overflow: hidden; }
  body {
    background: var(--backdrop);
    display: flex;
    align-items: center;
    justify-content: center;
    gap: 48px;
    font-family: "Roboto", Arial, sans-serif;
  }
  .card {
    position: relative;
    width: 530px;
    height: 303px;
    background: var(--card);
    border-bottom: 3px solid var(--gold-edge);
    box-shadow: 0 10px 24px rgba(0,0,0,0.18);
  }

  /* Front */
  .card-front { display: flex; align-items: center; }
  .brand {
    width: 250px;
    display: flex;
    flex-direction: column;
    align-items: center;
    gap: 12px;
  }
  .brand-mark {
    width: 18px; height: 18px;
    border: 2px solid var(--gold);
    border-radius: 50%;
    flex: none;
  }
  .brand-name {
    font-weight: 400;
    color: var(--gold);
    text-align: center;
    font-size: 24px;
    line-height: 1.2;
  }
  .divider {
    width: 1px;
    height: 190px;
    background: #9a9a9a;
  }
  .details { padding-left: 28px; color: var(--ink); }
  .person-name {
    font-weight: 700;
    font-size: 20px;
    color: var(--gold);
    text-transform: uppercase;
  }
  .person-title {
    font-size: 14px;
    color: var(--muted);
    text-transform: uppercase;
    margin-bottom: 12px;
  }
  .address { font-size: 13.5px; line-height: 1.3; margin-bottom: 6px; font-style: normal; }
  .contact { list-style: none; font-size: 13.5px; line-height: 1.35; }
  .contact li { display: flex; align-items: center; gap: 8px; }
  .contact svg { width: 11px; height: 11px; fill: var(--gold); flex: none; }

  /* Back */
  .card-back {
    display: flex;
    align-items: center;
    justify-content: center;
  }
  .back-name {
    font-weight: 400;
    color: var(--gold);
    font-size: 30px;
    display: flex;
    align-items: center;
    gap: 14px;
  }
  .back-name .brand-mark { width: 22px; height: 22px; }
  .badges {
    position: absolute;
    top: 44px; right: 40px;
    display: flex; gap: 8px;
  }
  .badge { height: 24px; background: var(--badge-red); border-radius: 2px; }
  .badge-scheme { width: 50px; }
  .badge-member { width: 56px; }
  .web-line {
    position: absolute;
    bottom: 34px; left: 0; right: 0;
    text-align: center;
    font-size: 12px;
    letter-spacing: 0.35em;
    color: var(--ink);
  }
</style>
</head>
<body>
  <section class="card card-front" aria-label="Business card front">
    <div class="brand">
      <span class="brand-mark"></span>
      <p class="brand-name">Ferncastle<br>Holdings</p>
    </div>
    <div class="divider"></div>
    <div class="details">
      <p class="person-name">Daniel Ashworth</p>
      <p class="person-title">CEO/Founder</p>
      <address class="address">
        Ferncastle Holdings Limited<br>
        The Willows<br>
        Ashby Rise, Ashby<br>
        GL52 7TN
      </address>
      <ul class="contact">
        <li><svg viewBox="0 0 24 24"><path d="M6.6 10.8a15 15 0 0 0 6.6 6.6l2.2-2.2c.3-.3.7-.4 1-.2 1.1.4 2.3.6 3.6.6.6 0 1 .4 1 1V20c0 .6-.4 1-1 1A17 17 0 0 1 3 4c0-.6.4-1 1-1h3.5c.6 0 1 .4 1 1 0 1.3.2 2.5.6 3.6.1.3 0 .7-.2 1z"/></svg>614 552 9087</li>
        <li><svg viewBox="0 0 24 24"><path d="M2 5h20v14H2zm2 2v.5l8 5 8-5V7z"/></svg>daniel@ferncastle.com</li>
        <li><svg viewBox="0 0 24 24"><circle cx="12" cy="12" r="10"/></svg>www.ferncastle.com</li>
      </ul>
    </div>
  </section>

  <section class="card card-back" aria-label="Business card back">
    <div class="badges">
      <span class="badge badge-scheme"></span>
      <span class="badge badge-member"></span>
    </div>
    <p class="back-name"><span class="brand-mark"></span>Ferncastle Holdings</p>
    <p class="web-line">www.ferncastle.com</p>
  </section>
</body>
</html>
```